デザインに特に指定はないのですが、インパクトがある感じを希望します。

CMSを使って簡単に作ってみました。
これを装飾して、ヘッダーをカッコよくしてくればいいと思います。

■イメージサイト
https://qomiru.jp/s/t-velmo

添付のPDFは内容は同じです。

下記が、最近作ったサイトです。
参考にしてください。

■参考サイト
https://qomiru.jp/s/KwLtoVeq

■下記に弊社の素材集が集まってます。

こちらの素材は自由に使ってもらっていいです。

会社素材サイトです
https://qomiru.jp/s/9Hn3YsuD

ワイヤーフレームを作り替えました。

それに合わせて、来週の月曜日まで延長しましたので、

ぜひ、よろしくお願いします。
間違えて、請求書をUPしてますが、無視してください。

新しい参考デザインは、

新デザイン 01.02 です。

よろしくお願いします。

ヘッダーだけですと他にも良い提案があったのですが、全体的に作り込まれていて、すぐに使える部分を評価しました。

ミトラノは、いつも使わせていただいてますが、この瞬間に申し訳ないと思います。他の方のデザインがあってこそ、最終的によいデザインが完成していると思います。ご提案ありがとうございました。

```html
<!DOCTYPE html>
<html lang="ja">
<head>
<meta charset="utf-8">
<title>受信率アクセル｜コミル メール配信機能</title>
<link href="https://fonts.googleapis.com/css2?family=Noto+Sans+JP:wght@400;500;700;900&family=Noto+Serif+JP:wght@700;900&display=swap" rel="stylesheet">
<style>
:root{
  --navy:#0b1a45;
  --navy-deep:#050d2a;
  --blue:#1556b8;
  --blue-dark:#0c3a86;
  --blue-line:#2a63c4;
  --red:#d0121b;
  --teal:#1fa6b4;
  --teal-dark:#137f8c;
  --yellow:#fff04a;
  --green:#27a52c;
  --green-dark:#13791a;
  --text:#222;
  --paper:#f6f8fc;
  --page:#ffffff;
}
*{box-sizing:border-box;margin:0;padding:0}
html,body{width:1200px;height:5400px;overflow:hidden}
body{background:#eef0f4;font-family:"Noto Sans JP",sans-serif;color:var(--text);font-size:13px;line-height:1.6}
.page{width:1200px;height:5400px;overflow:hidden;position:relative}

/* header */
.hero{height:380px;background:linear-gradient(180deg,var(--navy-deep),var(--navy) 60%,#1a2f66);position:relative;overflow:hidden}
.hero-skyline{position:absolute;left:0;right:0;bottom:0;height:150px;background:linear-gradient(180deg,rgba(40,70,140,0),rgba(60,90,160,.55))}
.hero-inner{width:640px;margin:0 auto;position:relative;height:100%}
.hero-tag{position:absolute;left:0;top:18px;display:flex;align-items:center;gap:8px;color:#fff;font-weight:700;font-size:15px}
.hero-tag .urgent{background:var(--red);border-radius:50%;width:46px;height:46px;display:flex;align-items:center;justify-content:center;font-size:13px;transform:rotate(-10deg)}
.hero-sub{position:absolute;left:20px;top:76px;color:#e8c34a;font-weight:900;font-size:19px;letter-spacing:.3em}
.hero-title{position:absolute;left:14px;top:104px;color:#fff;font-weight:900;font-size:74px;line-height:1.02;letter-spacing:.02em;text-shadow:0 3px 0 #0a1d55}
.hero-rate-label{position:absolute;left:20px;top:264px;color:#fff;font-weight:700;font-size:16px;letter-spacing:.1em}
.hero-rates{position:absolute;left:20px;top:290px;display:flex;gap:18px;color:#fff}
.rate span{display:block;font-size:12px;font-weight:700}
.rate b{font-size:46px;font-weight:900;color:#dfe6f6;font-style:italic;line-height:1}
.rate b small{font-size:20px;background:var(--red);border-radius:50%;padding:2px 5px;font-style:normal;color:#fff}
.hero-rates .tail{align-self:flex-end;font-size:12px;font-weight:700}
.hero-person{position:absolute;right:-10px;top:0;width:240px;height:380px;background:linear-gradient(180deg,#3a4c78,#6b7892 55%,#8d96a8)}
.hero-laptop{position:absolute;right:-30px;bottom:14px;width:130px;height:92px;background:linear-gradient(180deg,#cfd6e3,#8e99ad);border-radius:6px}

/* column */
.col{width:640px;margin:0 auto;background:var(--page);padding:14px 0 40px}

.alert{margin:0 8px;border:3px solid var(--red);background:#fff}
.alert-head{background:var(--red);color:#fff;font-weight:900;font-size:17px;padding:4px 14px;display:flex;gap:20px;align-items:center}
.alert-head span{font-size:12px;font-weight:700;letter-spacing:.2em}
.alert-body{display:flex;gap:14px;padding:12px 14px}
.alert-icon{width:86px;height:70px;flex:none;background:linear-gradient(180deg,#dfe6f2,#9fb0cc);border-radius:4px}
.alert-body p{font-size:12px;line-height:1.55}
.alert-body .red{color:var(--red);font-weight:700}

.match{margin:22px 8px 0;border:2px solid var(--blue-line);position:relative}
.match-head{background:linear-gradient(90deg,var(--blue-dark),var(--blue));color:#fff;font-weight:900;font-size:22px;padding:8px 0 8px 200px;position:relative}
.match-head .badge{position:absolute;left:-6px;top:-12px;background:var(--navy);color:#fff;font-size:17px;padding:4px 14px;transform:rotate(-6deg)}
.match-body{display:flex;height:236px}
.match-photo{width:230px;flex:none;background:linear-gradient(180deg,#c8ced8,#7b8699)}
.checks{list-style:none;flex:1;margin:10px 10px 10px -30px;border:2px solid var(--blue-line);background:#fff;position:relative}
.checks li{display:flex;align-items:center;gap:8px;padding:7px 10px;border-bottom:1px dotted #9ab;font-size:14px;color:var(--blue-dark);font-weight:500}
.checks li:last-child{border-bottom:none}
.checks li b{font-weight:900}
.checks svg{flex:none}

.lead{text-align:center;margin-top:26px}
.lead-top{font-weight:700;font-size:16px}
.lead-main{color:var(--red);font-weight:900;font-size:38px;line-height:1.25;margin-top:6px}
.lead-main .u{border-bottom:4px solid var(--red)}
.lead-main .s{font-size:26px;color:var(--text)}

.video-title{text-align:center;font-family:"Noto Serif JP",serif;color:var(--blue-dark);font-weight:900;font-size:28px;line-height:1.35;margin-top:30px}
.video{width:540px;height:300px;margin:18px auto 0;background:#1a1a1a;display:flex;align-items:center;justify-content:center}
.video-btn{width:52px;height:36px;background:#fff;border-radius:6px;display:flex;align-items:center;justify-content:center}

.block{margin:30px 8px 0;border:2px solid var(--blue-line);background:var(--paper)}
.block-head{background:linear-gradient(90deg,var(--blue-dark),var(--blue));color:#fff;font-weight:900;font-size:24px;line-height:1.35;padding:14px 22px 18px;position:relative}
.block-head::after{content:"";position:absolute;left:50%;bottom:-18px;margin-left:-22px;border-left:22px solid transparent;border-right:22px solid transparent;border-top:18px solid var(--blue-dark)}
.block-body{padding:30px 26px 22px;font-size:12.5px;line-height:1.75}
.block-body p{margin-bottom:8px}
.float-img{float:left;width:200px;height:120px;margin:0 18px 10px 0;background:linear-gradient(180deg,#d8e5f5,#7fa7d9)}
.float-img.right{float:right;margin:0 0 10px 18px;width:180px;height:170px;background:linear-gradient(180deg,#f2f2f2,#c9c9c9)}
.clear{clear:both}
.mark{background:linear-gradient(transparent 40%,var(--yellow) 40%);font-weight:700}
.mark-red{background:linear-gradient(transparent 40%,var(--yellow) 40%);color:var(--red);font-weight:700}
.big{font-size:15.5px;font-weight:700}
.red{color:var(--red)}

.booster{margin:30px 8px 0;background:linear-gradient(180deg,var(--teal),var(--teal-dark));padding:20px 24px 26px;position:relative}
.booster-art{height:190px;background:linear-gradient(180deg,#7fd3dc,#34a9b7);position:relative}
.booster-title{position:absolute;left:20px;top:26px;font-weight:900;color:var(--navy);font-size:46px;line-height:1.1;text-shadow:0 2px 0 #fff}
.booster-title small{font-size:17px;color:#fff;background:var(--red);display:inline-block;padding:2px 10px;margin-bottom:6px;text-shadow:none}
.booster-title em{display:block;font-style:normal;font-size:24px;color:#fff;text-shadow:none;margin-top:4px}
.booster-card{background:#fff;padding:20px 22px;margin-top:14px;font-size:12.5px;line-height:1.75}
.booster-card .result{color:var(--red);font-weight:900;font-size:18px;line-height:1.4;margin:6px 0}

.notice{text-align:center;color:var(--red);font-weight:900;font-size:17px;line-height:1.5;margin-top:20px}

.fit{margin:22px 8px 0;border:2px solid var(--blue-line);background:linear-gradient(180deg,#d3d8e2,#aab3c4)}
.fit-head{font-weight:900;color:var(--blue-dark);font-size:28px;padding:10px 0 4px 40px}
.fit .checks{margin:6px 40px 18px 40px}
.fit .checks li{font-size:17px;padding:10px 14px}

.cta-text{text-align:center;color:var(--red);font-weight:700;font-size:15px;line-height:1.6;margin-top:18px}
.cta{display:flex;align-items:center;justify-content:center;gap:40px;width:480px;height:100px;margin:20px auto 0;background:linear-gradient(180deg,#4cc34f,var(--green) 50%,var(--green-dark));border:3px solid #1a5f1e;border-radius:8px;color:#fff;text-decoration:none}
.cta-label small{display:block;font-size:14px;font-weight:700;text-align:center}
.cta-label b{font-size:30px;font-weight:900}

.faq-title{text-align:center;color:var(--blue-dark);font-weight:900;font-size:22px;margin-top:30px}
.faq{margin:14px 8px 0}
.faq dt{background:var(--blue);color:#fff;font-weight:700;font-size:15px;padding:8px 14px;display:flex;gap:12px}
.faq dd{padding:10px 14px;font-size:12px;display:flex;gap:12px;border-bottom:1px solid #dde}
.faq .q,.faq .a{font-weight:900;font-size:20px;line-height:1}
.faq .a{color:var(--blue)}

.form-title{text-align:center;color:var(--blue-dark);font-weight:700;font-size:17px;margin-top:26px}
.form-title small{font-size:12px;margin-right:8px}
.form{margin:12px 8px 0;border:4px solid var(--blue);padding:18px 26px 24px}
.row{display:flex;align-items:center;border-bottom:1px solid #e2e2e2;height:50px}
.row label{width:210px;font-size:13px;display:flex;align-items:center;gap:8px}
.req{background:var(--red);color:#fff;font-size:10px;padding:1px 5px}
.row label a{font-size:10px;color:var(--blue);text-decoration:underline}
.row .input{flex:1;height:34px;border:1px solid #bbb;background:#fff}
.row .radios{flex:1;display:flex;gap:18px;font-size:12px;align-items:center}
.radio{display:inline-block;width:12px;height:12px;border:1px solid #888;border-radius:50%;vertical-align:-2px;margin-right:4px}
.radio.on{border-color:var(--blue);box-shadow:inset 0 0 0 3px #fff;background:var(--blue)}
.submit{display:block;width:180px;height:46px;margin:22px auto 0;background:var(--teal);color:#fff;border:none;border-radius:4px;font-weight:700;font-size:15px;font-family:inherit}
</style>
</head>
<body>
<div class="page">

<header class="hero">
  <div class="hero-skyline" role="img" aria-label="夜景の街並みの背景"></div>
  <div class="hero-inner">
    <div class="hero-tag"><span class="urgent">緊急！</span>受信率を完全攻略！！</div>
    <div class="hero-sub">コミル メール配信機能</div>
    <h1 class="hero-title">受信率<br>アクセル</h1>
    <div class="hero-rate-label">受信フォルダーへの到達率</div>
    <div class="hero-rates">
      <div class="rate"><span>Hoshimail</span><b>98.<small>3%</small></b></div>
      <div class="rate"><span>Nimail</span><b>84.<small>3%</small></b></div>
      <div class="tail">を叩き出しました。</div>
    </div>
    <div class="hero-person" role="img" aria-label="拳を掲げるスーツ姿の男性の写真"></div>
    <div class="hero-laptop" role="img" aria-label="メール画面を表示したノートパソコンのイラスト"></div>
  </div>
</header>

<main class="col">

  <section class="alert">
    <div class="alert-head">超重要<span>―― ご注意ください ――</span></div>
    <div class="alert-body">
      <div class="alert-icon" role="img" aria-label="メール封筒のイラスト"></div>
      <p><span class="red">巷で謳われている「到達率」は、受信フォルダーだけではなく、迷惑メールフォルダーへの受信もカウントしています。</span><br>コミルの受信率UPアクセルは、純粋に、<span class="red">受信フォルダーへの到達率</span>が、Hoshimail 98.3%、Nimail 84.3%です。<br>この驚異の数字が理解できる情報配信者さまは、最後までご確認ください。</p>
    </div>
  </section>

  <section class="match">
    <div class="match-head"><span class="badge">どれか一つでも</span>当てはまる人は、必見です。</div>
    <div class="match-body">
      <div class="match-photo" role="img" aria-label="スーツ姿で考え込む男性の写真"></div>
      <ul class="checks">
        <li><svg width="18" height="18" viewBox="0 0 18 18"><rect x="1" y="3" width="14" height="14" fill="#fff" stroke="#333"/><path d="M3 9l4 4 9-11" fill="none" stroke="#d0121b" stroke-width="3"/></svg><span><b>受信率 UP アクセル</b>が、素直に驚異だと感じた</span></li>
        <li><svg width="18" height="18" viewBox="0 0 18 18"><rect x="1" y="3" width="14" height="14" fill="#fff" stroke="#333"/><path d="M3 9l4 4 9-11" fill="none" stroke="#d0121b" stroke-width="3"/></svg><span><b>1 年以上メルマガ発行</b>をしている</span></li>
        <li><svg width="18" height="18" viewBox="0 0 18 18"><rect x="1" y="3" width="14" height="14" fill="#fff" stroke="#333"/><path d="M3 9l4 4 9-11" fill="none" stroke="#d0121b" stroke-width="3"/></svg><span>定期的に、<b>メルマガ読者が増えている</b></span></li>
        <li><svg width="18" height="18" viewBox="0 0 18 18"><rect x="1" y="3" width="14" height="14" fill="#fff" stroke="#333"/><path d="M3 9l4 4 9-11" fill="none" stroke="#d0121b" stroke-width="3"/></svg><span>定期的に、<b>メルマガを配信し続けている</b></span></li>
        <li><svg width="18" height="18" viewBox="0 0 18 18"><rect x="1" y="3" width="14" height="14" fill="#fff" stroke="#333"/><path d="M3 9l4 4 9-11" fill="none" stroke="#d0121b" stroke-width="3"/></svg><span><b>メルマガからの収入がある</b></span></li>
      </ul>
    </div>
  </section>

  <section class="lead">
    <p class="lead-top">＼ このページの内容を実行していただければ、あなたの ／</p>
    <p class="lead-main">メルマガの反応率を<br><span class="u">一気に上げる</span><span class="s">ことができます。</span></p>
  </section>

  <section>
    <h2 class="video-title">まずは、現在の配信アルゴリズムと、<br>その対応方法をご確認ください。</h2>
    <div class="video"><div class="video-btn"><svg width="14" height="16" viewBox="0 0 14 16"><path d="M0 0l14 8-14 8z" fill="#222"/></svg></div></div>
  </section>

  <section class="block">
    <h2 class="block-head">開発者が決めたルールを徹底的に守れば、<br>生き残り、そして稼ぐことができる</h2>
    <div class="block-body">
      <div class="float-img" role="img" aria-label="検索画面とモニターのイラスト"></div>
      <p>メールの到達率は、検索エンジン対策と同じです。<br>毎年、配信アルゴリズムが変わります。<br>そのルールにメルマガ配信者も合わせる必要があります。<br>SEO対策とまったく同じです。検索エンジンのルールを決めている人が支配者です。</p>
      <div class="clear"></div>
      <p>その支配者に逆らって、まったくお門違いなことをしていては、<br>上位検索に引っかかるどころか、完全に検索圏外になってしまいますよね？<br>ここを、まずはしっかりと理解しなくてはいけません。</p>
      <p><span class="mark-red">場のルールに逆らっては、私たちのビジネスは成立しない</span>ということを。</p>
      <p>もう一度、お伝えします。<br><span class="mark big">メールの到達率は、検索エンジン対策と同じ</span>です。<br><span class="mark-red">配信アルゴリズムを決めている支配者に、１mmも逆らってはいけません。</span></p>
      <p>まずは、動画でお伝えしている内容を把握し、<br>あなたの配信内容、方法を、今の配信アルゴリズムにしっかりと合わせてください。</p>
    </div>
  </section>

  <section class="block">
    <h2 class="block-head">「到達率は、売上に直結する」<br>に、もっと敏感になる必要がある</h2>
    <div class="block-body">
      <div class="float-img right" role="img" aria-label="右肩上がりの棒グラフを描く手のイラスト"></div>
      <p>どのビジネスでも、情報配信を絡めることにより、<br>その売上は、驚くほど簡単に、2倍にも3倍にもなります。<br>これは、情報配信をおこなっている人であれば、実感していると思います。</p>
      <p>そして、情報配信の命は、「到達率」。<br>当然、到達率により、売上もびっくりするほど変動しますよね。</p>
      <div class="clear"></div>
      <p>なのに、<span class="mark-red">情報配信の主軸となるメルマガ配信に関しては、SEO対策のように、ルールに合わせるということをしっかりとやれないのは、なぜでしょうか？</span></p>
      <p>これは、メルマガが売上に直結しすぎているのが、原因のひとつかもしれません。<br><span class="big">メルマガ配信すれば、売上が簡単にあがる。<br>それがクッキリハッキリしているから、少しのルールを破ってでも、配信してしまいます。</span></p>
      <p><span class="mark-red">その配信の繰り返しが、結局は、自分自身を苦しめることになるとも知らずに。</span></p>
    </div>
  </section>

  <section class="block">
    <h2 class="block-head">一度ハマると、<br>戻るまで、かなり時間がかかります</h2>
    <div class="block-body">
      <div class="float-img" role="img" aria-label="下降する折れ線グラフのイラスト"></div>
      <p>弊社サポートにも、到達率に関するお問い合わせは、ポツポツといただきます。<br>現状を確認し、対応方法をお伝えし、様子をみていただきます。</p>
      <div class="clear"></div>
      <p>「まったく変わらないのですがなんとかしてください！」と連絡をいただくことがあります。<br>それは、そうです。お伝えしましたよね？<br><span class="mark big">メールの到達率は、検索エンジン対策と同じ</span>です。</p>
      <p>圏外に突き落とされたサイトが、対策をし直し、数日で上位検索にかかることはありますか？<br>そんな夢のような話は聞いたことが無いはずです。<br>一度ハマると、戻るまでかなり時間がかかる。<br>残念ながら、この部分も検索エンジンと同じです。<br>そこをどうにか出来ないか？<br>考えに考え抜いて開発したのが、今回のシステムです。</p>
    </div>
  </section>

  <section class="booster">
    <div class="booster-art" role="img" aria-label="親指を立てる男性と利用者のイラスト">
      <div class="booster-title"><small>手遅れになる前に！！</small><br>受信率UPアクセル<em>を開発しました</em></div>
    </div>
    <div class="booster-card">
      <p>まずは、これまでお伝えしたことは、しっかりと意識をしてメルマガ運営をしてください。<br>そして、動画でお伝えしている「プラス要因」と「マイナス要因」の対策。<br>ひとつひとつは、非常にシンプルな内容だと思います。確実に対応をしていきましょう。<br>最新のアルゴリズムへの対応ですが、そこをコミルがおこないます。</p>
      <p>手動では面倒な部分を、コミルの新機能で、最適化します。<br>これにより、</p>
      <p class="result">受信フォルダーへの到達率がHoshimail98.3%、Nimail84.3%という、</p>
      <p>驚異の数字を叩き出すことが出来ています。<br>情報配信が、収益の柱の１つとして、重要なポジションだとお考えの方なら、<br>かなり重宝されるシステムです。ぜひご活用ください。</p>
    </div>
  </section>

  <p class="notice">【 重 要 】全ての方に効果がある機能ではありません。<br><span style="font-size:14px">メルマガ運営で収益化ができている方に、有効な機能となります。</span></p>

  <section class="fit">
    <h2 class="fit-head">＼ 受信率UPアクセルが有効な方 ／</h2>
    <ul class="checks">
      <li><svg width="20" height="20" viewBox="0 0 18 18"><rect x="1" y="3" width="14" height="14" fill="#fff" stroke="#333"/><path d="M3 9l4 4 9-11" fill="none" stroke="#d0121b" stroke-width="3"/></svg><span><b>1 年以上メルマガ発行</b>をしている</span></li>
      <li><svg width="20" height="20" viewBox="0 0 18 18"><rect x="1" y="3" width="14" height="14" fill="#fff" stroke="#333"/><path d="M3 9l4 4 9-11" fill="none" stroke="#d0121b" stroke-width="3"/></svg><span>定期的に、<b>メルマガ読者が増えている</b></span></li>
      <li><svg width="20" height="20" viewBox="0 0 18 18"><rect x="1" y="3" width="14" height="14" fill="#fff" stroke="#333"/><path d="M3 9l4 4 9-11" fill="none" stroke="#d0121b" stroke-width="3"/></svg><span>定期的に、<b>メルマガを配信し続けている</b></span></li>
      <li><svg width="20" height="20" viewBox="0 0 18 18"><rect x="1" y="3" width="14" height="14" fill="#fff" stroke="#333"/><path d="M3 9l4 4 9-11" fill="none" stroke="#d0121b" stroke-width="3"/></svg><span><b>メルマガからの収入がある</b></span></li>
    </ul>
  </section>

  <p class="cta-text">上記に当てはまり、到達率の低下が気になる方は、<br>まずは、アクセルの効果があるかを確認いたします。<br>下記フォームより、調査依頼の申請をお願いいたします。</p>

  <a class="cta" href="#form">
    <span class="cta-label"><small>受信率UPアクセル効果</small><b>調査を依頼する</b></span>
    <svg width="22" height="34" viewBox="0 0 22 34"><path d="M4 3l14 14L4 31" fill="none" stroke="#fff" stroke-width="5"/></svg>
  </a>

  <h2 class="faq-title">よくある質問</h2>
  <dl class="faq">
    <dt><span class="q">Q</span>このシステムはコミルのみで使えるのですか？</dt>
    <dd><span class="a">A</span>はい。コミルのメール配信機能のオプションとしてご提供するため、コミルのみで使用が可能となります。</dd>
    <dt><span class="q">Q</span>メルマガを運営して、まだ日が浅いですが、このオプションは利用できますか？</dt>
    <dd><span class="a">A</span>メルマガ運営したての方には、不要なシステムです。受信率UPアクセルが有効な方は、1年以上メルマガを運営し、定期的に配信を続けている方となります。まずは、動画でお伝えしている内容を実践してみてください。</dd>
    <dt><span class="q">Q</span>このシステムの詳細を教えてください。</dt>
    <dd><span class="a">A</span>内部ロジックの露出となるので、詳細を一般公開することはできません。調査依頼の結果、アクセルが必要と感じた方に、詳細をお伝えしております。</dd>
  </dl>

  <h2 class="form-title" id="form"><small>受信率UPアクセル</small>調査依頼フォーム</h2>
  <form class="form">
    <div class="row"><label><span class="req">必須</span>コミルID <a>確認方法はこちら</a></label><span class="input"></span></div>
    <div class="row"><label><span class="req">必須</span>メルマガID <a>確認方法はこちら</a></label><span class="input"></span></div>
    <div class="row"><label><span class="req">必須</span>ご担当者氏名</label><span class="input"></span></div>
    <div class="row"><label><span class="req">必須</span>電話番号</label><span class="input"></span></div>
    <div class="row"><label><span class="req">必須</span>お電話可能な時間帯</label><span class="radios"><span><i class="radio"></i>平日AM</span><span><i class="radio"></i>平日PM（17時まで）</span><span><i class="radio on"></i></span></span></div>
    <div class="row"><label><span class="req">必須</span>メールアドレス</label><span class="input"></span></div>
    <button class="submit" type="button">送信する</button>
  </form>

</main>
</div>
</body>
</html>
```